Brambleton Law Stationary - Law Firm

I am looking for a designer who can help me design letterhead and envelopes consistent with our new business cards. Feel free to reach out to me directly at ned@brambletonlaw.example. Thank you!! Visit brambletonlaw.example to see our site and the attached files for creative assets.

Target Market(s)

Anyone needing a lawyer

Font styles to use
Other font styles liked:
• Adobe Caslon Pro

Requirements
Must have
• Adobe Caslon Pro font
Full color
Nice to have
• My photo on front along with 2/3 face of camo - see mock up for example of what I have in mind.

American colors - similar to the ones found on my website and gold.

```html
<!DOCTYPE html>
<html lang="en">
<head>
<meta charset="utf-8">
<title>Brambleton Law Letterhead</title>
<link rel="stylesheet" href="https://fonts.googleapis.com/css2?family=Libre+Caslon+Text:ital,wght@0,400;0,700;1,400&display=swap">
<style>
  :root {
    --backdrop: #3d3a3b;
    --navy: #23295e;
    --gold: #a8945a;
    --paper: #e9edef;
    --red: #c1272d;
    --white: #ffffff;
    --suit-dark: #1f2226;
    --suit-light: #5a5f66;
    --camo-dark: #2c2a22;
    --camo-light: #8a7c4e;
  }
  * { margin: 0; padding: 0; box-sizing: border-box; }
  html, body {
    width: 1200px;
    height: 955px;
    overflow: hidden;
    background: var(--backdrop);
  }
  .canvas {
    width: 1200px;
    height: 955px;
    display: flex;
    align-items: center;
    justify-content: center;
  }
  .letterhead {
    position: relative;
    width: 642px;
    height: 894px;
    background: var(--paper);
    font-family: "Libre Caslon Text", "Times New Roman", serif;
    overflow: hidden;
    box-shadow: 0 6px 18px rgba(0,0,0,0.35);
  }
  .masthead {
    position: absolute;
    inset: 0 0 auto 0;
    height: 134px;
    background: var(--navy);
  }
  .brand-mark {
    position: absolute;
    left: 30px;
    top: 40px;
    width: 44px;
    height: 44px;
    border: 3px solid var(--gold);
  }
  .firm-name {
    position: absolute;
    left: 100px;
    top: 58px;
    font-size: 30px;
    font-weight: 700;
    color: var(--gold);
    letter-spacing: 0.3px;
    text-transform: uppercase;
    line-height: 1;
  }
  .firm-address {
    position: absolute;
    left: 101px;
    top: 95px;
    font-size: 11px;
    font-weight: 400;
    color: var(--white);
    line-height: 1;
  }
  .tagline {
    position: absolute;
    right: 30px;
    top: 106px;
    font-size: 14px;
    font-style: italic;
    font-weight: 400;
    color: var(--white);
    line-height: 1;
  }
  .footer-band {
    position: absolute;
    left: 0;
    right: 0;
    bottom: 0;
    height: 40px;
    background: var(--red);
  }
  .mission {
    position: absolute;
    left: 110px;
    right: 88px;
    bottom: 12px;
    text-align: center;
    font-size: 15px;
    font-weight: 400;
    color: var(--white);
    line-height: 1;
  }
  .attorney-photo {
    position: absolute;
    left: 0;
    bottom: 0;
    width: 110px;
    height: 182px;
    background: linear-gradient(180deg, var(--paper) 0%, var(--suit-light) 30%, var(--suit-dark) 100%);
  }
  .camo-photo {
    position: absolute;
    right: 0;
    bottom: 6px;
    width: 88px;
    height: 139px;
    background: linear-gradient(160deg, var(--camo-light) 0%, var(--camo-dark) 100%);
  }
</style>
</head>
<body>
  <main class="canvas">
    <article class="letterhead">
      <header class="masthead">
        <span class="brand-mark"></span>
        <h1 class="firm-name">Brambleton Law</h1>
        <p class="firm-address">48 W. Larkspur Avenue Fairhaven, Vermont 05743</p>
        <p class="tagline">A Family Founded Law Office</p>
      </header>
      <footer>
        <div class="footer-band"></div>
        <p class="mission">Our Pledge: To Stand Up for You</p>
        <div class="attorney-photo" role="img" aria-label="Portrait photo of the attorney in a dark suit and blue tie"></div>
        <div class="camo-photo" role="img" aria-label="Photo of the attorney with camouflage face paint"></div>
      </footer>
    </article>
  </main>
</body>
</html>
```